New cool to-go cup for KELMO Coffee

UPDATE MARCH 18: Please read the attached document "Design ideas - Front" with a mock-up of the design we are looking for. And please don't change the logo.

We are looking for a new cool design for our to-go cups in kraft paper (same style as the attached photo).

The idea:

We have three different cups sizes: 6oz, 8oz and 12oz. We call them “Tiny-Lark” (6oz), “Mid-Wren” (8oz) and “Tall-heron” (12oz) (refers to the size in milliliters). We would like to include this in the cup design. Please see the attached sketch of the idea ("Design ideas - Front").

The backside of the cup should have the attached text and logo ("Design ideas - Back").

But other ideas are also very welcome too! Maybe just a simple cup with the logo.

Please keep the design very minimalistic. The more simple the better.

Target Market(s)

Young urban people

Industry/Entity Type

Coffee shop

Font styles to use
Sans Serif

Requirements
Must have
• Kraft paper cups

```html
<!DOCTYPE html>
<html lang="en">
<head>
<meta charset="utf-8">
<title>KELMO Coffee – to-go cup range</title>
<link rel="stylesheet" href="https://fonts.googleapis.com/css2?family=Montserrat:wght@400;700&display=swap">
<style>
  :root {
    --backdrop: #d0d0d0;
    --kraft-light: #b9a195;
    --kraft-dark: #a38c81;
    --cup-white: #fdfdfd;
    --ink: #141414;
    --ink-soft: #2a2522;
  }
  * { box-sizing: border-box; margin: 0; padding: 0; }
  html, body { width: 846px; height: 1200px; overflow: hidden; }
  body {
    position: relative;
    background: var(--backdrop);
    font-family: "Montserrat", Arial, sans-serif;
    color: var(--ink);
  }
  .cup { position: absolute; }
  .cup-shape { position: absolute; inset: 0; width: 100%; height: 100%; }
  .print {
    position: absolute; left: 0; right: 0;
    display: flex; flex-direction: column; align-items: center; text-align: center;
  }
  .brand-mark {
    display: flex; align-items: center; justify-content: center;
    border: 3px solid var(--ink); border-radius: 50%;
    font-weight: 700; letter-spacing: 0.12em; line-height: 1.25;
    color: var(--ink); text-transform: uppercase;
  }
  .size-name { letter-spacing: -0.01em; line-height: 1; }
  .size-name b { font-weight: 700; }
  .size-name span { font-weight: 400; }
  .story { color: var(--ink-soft); line-height: 1.35; }
  .web { font-weight: 700; color: var(--ink); }
  .handle { color: var(--ink-soft); }

  /* front, small */
  .front-small { left: 73px; top: 298px; width: 210px; height: 252px; }
  .front-small .print { top: 59px; }
  .front-small .brand-mark { width: 90px; height: 90px; font-size: 10px; }
  .front-small .size-name { font-size: 24px; margin-top: 12px; }
  /* front, medium */
  .front-medium { left: 296px; top: 261px; width: 226px; height: 292px; }
  .front-medium .print { top: 74px; }
  .front-medium .brand-mark { width: 90px; height: 90px; font-size: 10px; }
  .front-medium .size-name { font-size: 24px; margin-top: 12px; }
  /* front, large */
  .front-large { left: 540px; top: 214px; width: 233px; height: 345px; }
  .front-large .print { top: 101px; }
  .front-large .brand-mark { width: 90px; height: 90px; font-size: 10px; }
  .front-large .size-name { font-size: 24px; margin-top: 10px; }

  /* back, small */
  .back-small { left: 71px; top: 745px; width: 210px; height: 252px; }
  .back-small .print { top: 78px; }
  .back-small .size-name { font-size: 22px; }
  .back-small .story { font-size: 9.5px; margin-top: 8px; }
  .back-small .web { font-size: 9.5px; margin-top: 10px; }
  .back-small .handle { font-size: 9.5px; margin-top: 2px; }
  /* back, medium */
  .back-medium { left: 294px; top: 708px; width: 226px; height: 284px; }
  .back-medium .print { top: 98px; }
  .back-medium .size-name { font-size: 24px; }
  .back-medium .story { font-size: 11.5px; margin-top: 8px; }
  .back-medium .web { font-size: 11.5px; margin-top: 10px; }
  .back-medium .handle { font-size: 11.5px; margin-top: 2px; }
  /* back, large */
  .back-large { left: 538px; top: 662px; width: 233px; height: 345px; }
  .back-large .print { top: 131px; }
  .back-large .size-name { font-size: 24px; }
  .back-large .story { font-size: 11.5px; margin-top: 8px; }
  .back-large .web { font-size: 11.5px; margin-top: 10px; }
  .back-large .handle { font-size: 11.5px; margin-top: 2px; }
</style>
</head>
<body>
  <svg width="0" height="0" style="position:absolute" aria-hidden="true">
    <defs>
      <linearGradient id="kraft" x1="0" x2="1" y1="0" y2="0">
        <stop offset="0" stop-color="var(--kraft-dark)"/>
        <stop offset="0.4" stop-color="var(--kraft-light)"/>
        <stop offset="1" stop-color="var(--kraft-dark)"/>
      </linearGradient>
      <symbol id="cup" viewBox="0 0 100 100" preserveAspectRatio="none">
        <polygon points="12,84 88,84 86,100 14,100" fill="var(--cup-white)"/>
        <polygon points="5,6 95,6 88,86 12,86" fill="url(#kraft)"/>
        <rect x="0" y="0" width="100" height="7" rx="2" fill="var(--cup-white)"/>
      </symbol>
    </defs>
  </svg>

  <!-- front row -->
  <div class="cup front-small">
    <svg class="cup-shape" aria-hidden="true"><use href="#cup"/></svg>
    <div class="print">
      <div class="brand-mark">Kelmo<br>Coffee</div>
      <p class="size-name"><b>tiny</b><span>lark</span></p>
    </div>
  </div>
  <div class="cup front-medium">
    <svg class="cup-shape" aria-hidden="true"><use href="#cup"/></svg>
    <div class="print">
      <div class="brand-mark">Kelmo<br>Coffee</div>
      <p class="size-name"><b>mid</b><span>wren</span></p>
    </div>
  </div>
  <div class="cup front-large">
    <svg class="cup-shape" aria-hidden="true"><use href="#cup"/></svg>
    <div class="print">
      <div class="brand-mark">Kelmo<br>Coffee</div>
      <p class="size-name"><b>tall</b><span>heron</span></p>
    </div>
  </div>

  <!-- back row -->
  <div class="cup back-small">
    <svg class="cup-shape" aria-hidden="true"><use href="#cup"/></svg>
    <div class="print">
      <p class="size-name"><b>#tiny</b><span>lark</span></p>
      <p class="story">Read about our coffee<br>and the dedicated farmers<br>who made this cup possible:</p>
      <p class="web">www.kelmocoffee.com</p>
      <p class="handle">@kelmocoffee.com</p>
    </div>
  </div>
  <div class="cup back-medium">
    <svg class="cup-shape" aria-hidden="true"><use href="#cup"/></svg>
    <div class="print">
      <p class="size-name"><b>#mid</b><span>wren</span></p>
      <p class="story">Read about our coffee<br>and the dedicated farmers<br>who made this cup possible:</p>
      <p class="web">www.kelmocoffee.com</p>
      <p class="handle">@kelmocoffee.com</p>
    </div>
  </div>
  <div class="cup back-large">
    <svg class="cup-shape" aria-hidden="true"><use href="#cup"/></svg>
    <div class="print">
      <p class="size-name"><b>#tall</b><span>heron</span></p>
      <p class="story">Read about our coffee<br>and the dedicated farmers<br>who made this cup possible:</p>
      <p class="web">www.kelmocoffee.com</p>
      <p class="handle">@kelmocoffee.com</p>
    </div>
  </div>
</body>
</html>
```